Real Estate Seller Financing Postcard

I need a postcard that lays out these options contained in the notes that grabs attention, explains the two options easily and is eye-catching. The front needs to have the percentages on it and information about it and on the other side One side exact Text is:
"Monthly income without tenant headaches" in big letters. Also on front "Get
110%
add an "or"
160% of market value for your property. ". The percentages should be displayed and that is not to be a sentence of text. Other side text: I need bullets points for these "Formal protection as a lien holder against home
No commission or closing cost
Fast closings possible
Property taken as is so no repairs.

Add to the top of the back in "It’s simple. I am a new investor without down payment capital who still want to double our portfolio this year to grow our portfolio."
Here are the two options that are to be the largest part of the back
Option 1, you can receive 80% now cash and 30% over a short period of time including interest.

Option 2, where act like a bank allowing you to make 150% if you finance the whole property(ies). No gimmicks and surprises, just simple unconventional financing.

Include Logo Somewhere

Target Market(s)

Property Owners Wanting to Sell Their Property

Industry/Entity Type

Real Estate Investing

Requirements
Must have
• The options promiment and each side with its respective information. Must have logo somewhere
Nice to have
• The options in color other than black.
Should not have
• A picture of money on the front. Any other image is okay.

```html
<!DOCTYPE html>
<html lang="en">
<head>
<meta charset="utf-8">
<title>Seller Financing Postcard – Meridian Real Estate Group</title>
<link href="https://fonts.googleapis.com/css2?family=Montserrat:wght@500;600;700&display=swap" rel="stylesheet">
<style>
  :root {
    --navy: #0b3a8c;
    --navy-deep: #082f78;
    --sky-top: #4fb2ea;
    --sky-light: #d7ecf8;
    --wood: #b98a5e;
    --stone: #e6e2da;
    --pool: #3fb7d8;
    --grey-dark: #4a4a4a;
    --grey-mid: #8d8d8d;
    --grey-light: #d9d9d9;
    --grass: #6aa83a;
    --grass-light: #a9cf6e;
  }
  html, body {
    margin: 0;
    padding: 0;
    width: 1200px;
    height: 799px;
    overflow: hidden;
    background: #ffffff;
  }
  .postcard {
    display: block;
    width: 1200px;
    height: 799px;
  }
  .headline {
    font-family: "Montserrat", sans-serif;
    font-weight: 600;
    font-size: 92px;
    fill: var(--navy);
  }
  .offer-small {
    font-family: "Montserrat", sans-serif;
    font-weight: 600;
    fill: var(--navy);
  }
  .offer-figure {
    font-family: "Montserrat", sans-serif;
    font-weight: 700;
    fill: var(--navy);
    letter-spacing: -4px;
  }
  .offer-note {
    font-family: "Montserrat", sans-serif;
    font-weight: 500;
    font-size: 27px;
    fill: var(--navy);
  }
  .brand-name {
    font-family: "Montserrat", sans-serif;
    font-weight: 500;
    fill: var(--navy);
  }
  .frame-line {
    fill: none;
    stroke: var(--navy);
  }
</style>
</head>
<body>
<svg class="postcard" viewBox="0 0 1502 1000" width="1200" height="799" xmlns="http://www.w3.org/2000/svg">
  <defs>
    <linearGradient id="backdropTone" x1="0" y1="0" x2="0" y2="1">
      <stop offset="0" stop-color="#bdbdbd"/>
      <stop offset="0.45" stop-color="#7a7a7a"/>
      <stop offset="0.62" stop-color="var(--grey-dark)"/>
      <stop offset="0.75" stop-color="var(--grey-mid)"/>
      <stop offset="1" stop-color="var(--grey-light)"/>
    </linearGradient>
    <linearGradient id="houseTone" x1="0" y1="0" x2="0" y2="1">
      <stop offset="0" stop-color="var(--sky-top)"/>
      <stop offset="0.45" stop-color="var(--sky-light)"/>
      <stop offset="0.62" stop-color="var(--wood)"/>
      <stop offset="0.85" stop-color="var(--stone)"/>
      <stop offset="1" stop-color="var(--pool)"/>
    </linearGradient>
    <linearGradient id="villaTone" x1="0" y1="0" x2="0" y2="1">
      <stop offset="0" stop-color="#8ccbf0"/>
      <stop offset="0.4" stop-color="#eef3f6"/>
      <stop offset="0.7" stop-color="#d9d6cf"/>
      <stop offset="1" stop-color="var(--grass)"/>
    </linearGradient>
    <linearGradient id="lawnTone" x1="0" y1="0" x2="0" y2="1">
      <stop offset="0" stop-color="var(--grass)"/>
      <stop offset="1" stop-color="var(--grass-light)"/>
    </linearGradient>
    <path id="noteArc" d="M1047,580 A200,200 0 0 0 1417,445"/>
  </defs>

  <!-- Backdrop -->
  <rect width="1502" height="1000" fill="url(#backdropTone)" role="img" aria-label="Soft black and white photo of a modern house with a lawn and stepping stones"/>

  <!-- Headline panel -->
  <path d="M0,0 L705,0 C800,80 850,250 825,400 C805,520 760,600 712,648 L0,648 Z"
        fill="url(#houseTone)" role="img" aria-label="Colour photo of a modern house with a pergola and pool under a blue sky"/>
  <path class="frame-line" stroke-width="8" d="M705,0 C800,80 850,250 825,400 C805,520 760,600 712,648"/>
  <rect x="0" y="643" width="716" height="15" fill="var(--navy)"/>

  <g class="headline">
    <text x="162" y="117">MONTHLY</text>
    <text x="330" y="235">INCOME</text>
    <text x="300" y="352">WITHOUT</text>
    <text x="355" y="469">TENANT</text>
    <text x="72" y="586">HEADACHES</text>
  </g>

  <!-- Offer bubbles -->
  <g class="offer-bubbles">
    <circle cx="1065" cy="255" r="190" fill="none" stroke="var(--navy)" stroke-width="14"/>
    <circle cx="1220" cy="480" r="225" fill="none" stroke="var(--navy)" stroke-width="14"/>
    <circle cx="1065" cy="255" r="190" fill="url(#villaTone)"/>
    <circle cx="1220" cy="480" r="225" fill="url(#villaTone)" role="img" aria-label="Colour photo of a modern two storey villa with a garden"/>
  </g>

  <text class="offer-small" x="1062" y="172" font-size="66" text-anchor="middle">Get</text>
  <text class="offer-figure" x="1068" y="305" font-size="122" text-anchor="middle">110%</text>
  <text class="offer-small" x="1205" y="400" font-size="62" text-anchor="middle">or</text>
  <text class="offer-figure" x="1215" y="548" font-size="128" text-anchor="middle">160%</text>
  <text class="offer-note">
    <textPath href="#noteArc" startOffset="50%" text-anchor="middle">of market value for your property</textPath>
  </text>

  <!-- Brand dome -->
  <ellipse cx="755" cy="1012" rx="415" ry="258" fill="url(#lawnTone)" role="img" aria-label="Photo of green lawn with square stepping stones"/>
  <ellipse class="frame-line" cx="755" cy="1012" rx="415" ry="258" stroke-width="8"/>

  <g class="brand">
    <circle cx="598" cy="893" r="72" fill="none" stroke="var(--navy)" stroke-width="3"/>
    <text class="brand-name" x="700" y="912" font-size="62">MERIDIAN</text>
    <text class="brand-name" x="702" y="948" font-size="25">REAL ESTATE GROUP</text>
  </g>
</svg>
</body>
</html>
```